Text heavy poster for university audience

I have developed a set of standards for online teaching that need to be turned into a post format. The project has a logo which should be incorporated. Most of the designing will be in terms of text layout. The logo (two versions - higher quality files available) and the a sample of standards (as image - word version available; the example is one third of standards) are attached. Design that can be adapted to brochure format would be great. (Brochure adaption will be paid separately via another project to be opened here). More details available here: http://www.brivelquarto.net
Updates

Dear all,

The URL for the site needs to be include in the design - either as footer or under logo:
<http://www.brivelquarto.net>

Sorry for late notice

Target Market(s)

The are university staff

Industry/Entity Type

University

Font styles to use
Serif
Sans Serif

Requirements
Must have
• The text in the "required" attachment must be included; but for initial draft feel free to restrict your design to "sample" attachment
The green from the Logo (PANTONE 17-5641 Emerald) should be the foundation of the colour palette.
Nice to have
• The collaborators as named here: http://www.brivelquarto.net/collaborators/
My preferred find is helvetica neue, but similar can be used
Should not have
• Decorative fonts

```html
<!DOCTYPE html>
<html lang="en">
<head>
<meta charset="utf-8">
<title>Brivel Quarto – Standards for Online Teaching</title>
<link href="https://fonts.googleapis.com/css2?family=Arimo:wght@400;700&family=Roboto+Condensed:wght@400;500;700&display=swap" rel="stylesheet">
<style>
:root{
  --emerald:#17966e;
  --emerald-head:#4aa57f;
  --good-head:#a9d5bf;
  --excellent-head:#e4f2eb;
  --threshold-cell:#cfd0d2;
  --good-cell:#e4e4e5;
  --excellent-cell:#f2f2f2;
  --ink:#1d1d1b;
  --rule:#6d6e70;
  --paper:#ffffff;
}
*{margin:0;padding:0;box-sizing:border-box}
html,body{width:848px;height:1200px;overflow:hidden;background:var(--paper)}
body{position:relative;font-family:"Arimo",Arial,sans-serif;color:var(--ink)}
.masthead{position:absolute;left:0;top:0;width:848px;height:157px;background:var(--emerald)}
.brand{position:absolute;left:462px;top:40px;display:flex;align-items:center;gap:22px}
.brand-square{width:78px;height:78px;background:var(--paper)}
.brand-name{font-family:"Roboto Condensed",Arial,sans-serif;font-weight:700;color:var(--paper);font-size:27px;line-height:32px;letter-spacing:.5px;text-transform:uppercase}
.authors{position:absolute;right:73px;top:173px;font-family:"Roboto Condensed",Arial,sans-serif;font-weight:700;font-size:22px;color:var(--emerald)}
.section-title{position:absolute;left:74px;font-family:"Roboto Condensed",Arial,sans-serif;font-weight:500;font-size:29px;color:var(--emerald);letter-spacing:-.2px}
.section-intro{position:absolute;left:75px;width:365px;font-size:8.3px;line-height:12px}
.section-intro b{font-weight:700}
.standard{position:absolute;width:210px}
.standard-title{font-family:"Roboto Condensed",Arial,sans-serif;font-weight:700;font-size:7.6px;line-height:9px;height:13px;white-space:nowrap;width:212px;overflow:hidden}
.standard-title.tight{font-size:6.4px;letter-spacing:-.15px}
.standard-title.two-line{height:22px;white-space:normal;width:200px}
.rubric{display:grid;grid-template-columns:70px 70px 70px;border:.6px solid var(--rule)}
.rubric span{font-size:6.6px;line-height:8.2px;padding:1px 3px;border-right:.6px solid var(--rule)}
.rubric span:nth-child(3n){border-right:none}
.rubric .head{height:12px;border-bottom:.6px solid var(--rule)}
.rubric .h-threshold{background:var(--emerald-head)}
.rubric .h-good{background:var(--good-head)}
.rubric .h-excellent{background:var(--excellent-head)}
.rubric .c-threshold{background:var(--threshold-cell);height:68px;padding-top:3px}
.rubric .c-good{background:var(--good-cell);height:68px;padding-top:3px}
.rubric .c-excellent{background:var(--excellent-cell);height:68px}
.col-1{left:75px}.col-2{left:315px}.col-3{left:555px}
.licence{position:absolute;left:75px;top:1143px;display:flex;align-items:center;gap:8px}
.licence-mark{width:14px;height:14px;border-radius:50%;border:1.5px solid var(--ink)}
.licence-name{font-family:"Arimo",Arial,sans-serif;font-weight:700;font-size:10px;line-height:9px;width:58px}
.licence-text{position:absolute;left:157px;top:1143px;width:620px;font-size:4.8px;line-height:7px}
</style>
</head>
<body>
<header class="masthead">
  <div class="brand"><div class="brand-square"></div><div class="brand-name">Brivel Quarto</div></div>
</header>
<p class="authors">Dana Whitlow and Collaborators</p>

<h2 class="section-title" style="top:208px">One: Students</h2>
<p class="section-intro" style="top:246px">Students are supported in their online learning with a quality <b>curriculum</b> [1-4], opportunities for <b>interaction with peers and staff</b> [5&amp;6], and appropriate <b>support</b> [7&amp;8].</p>

<div class="standard col-1" style="top:282px"><p class="standard-title">1. Curriculum materials are aligned, available and engaging</p>
<div class="rubric"><span class="head h-threshold">Threshold</span><span class="head h-good">Good</span><span class="head h-excellent">Excellent</span><span class="c-threshold">The necessary materials are constructively aligned and available online</span><span class="c-good">The materials are provided using a variety of media to engage students and support diversity</span><span class="c-excellent"></span></div></div>

<div class="standard col-2" style="top:282px"><p class="standard-title tight">4. Students are provided with timely, improvement focused formative feedback</p>
<div class="rubric"><span class="head h-threshold">Threshold</span><span class="head h-good">Good</span><span class="head h-excellent">Excellent</span><span class="c-threshold">Appropriate technologies are used to provide students with formative feedback in a timely manner</span><span class="c-good">Feedback is provided in a variety of media to engage students and support diversity</span><span class="c-excellent"></span></div></div>

<div class="standard col-3" style="top:282px"><p class="standard-title">7. Students are provided with appropriate learning support</p>
<div class="rubric"><span class="head h-threshold">Threshold</span><span class="head h-good">Good</span><span class="head h-excellent">Excellent</span><span class="c-threshold">Appropriate, up-to-date and reliable learning guides and resources are provided online</span><span class="c-good">A range of appropriate, up-to-date and reliable online learning skills workshops are available</span><span class="c-excellent"></span></div></div>

<div class="standard col-1" style="top:393px"><p class="standard-title">2. Learning activities are aligned, available and engaging</p>
<div class="rubric"><span class="head h-threshold">Threshold</span><span class="head h-good">Good</span><span class="head h-excellent">Excellent</span><span class="c-threshold">Constructively aligned learning activities are available online</span><span class="c-good">Learning activities use a variety of appropriate technologies to engage students and support diversity</span><span class="c-excellent"></span></div></div>

<div class="standard col-2" style="top:393px"><p class="standard-title">5. Students are provided with opportunities to interact with peers</p>
<div class="rubric"><span class="head h-threshold">Threshold</span><span class="head h-good">Good</span><span class="head h-excellent">Excellent</span><span class="c-threshold">There are opportunities for social interaction</span><span class="c-good">There are opportunities for learning-focused interaction</span><span class="c-excellent"></span></div></div>

<div class="standard col-3" style="top:393px"><p class="standard-title">1. Curriculum materials are aligned, available and engaging</p>
<div class="rubric"><span class="head h-threshold">Threshold</span><span class="head h-good">Good</span><span class="head h-excellent">Excellent</span><span class="c-threshold">The necessary materials are constructively aligned and available online</span><span class="c-good">The materials are provided using a variety of media to engage students and support diversity</span><span class="c-excellent"></span></div></div>

<div class="standard col-1" style="top:504px"><p class="standard-title">3. Assessment tasks are aligned, available and engaging</p>
<div class="rubric"><span class="head h-threshold">Threshold</span><span class="head h-good">Good</span><span class="head h-excellent">Excellent</span><span class="c-threshold">Constructively aligned assessment tasks are available online</span><span class="c-good">Assessment tasks use a variety of appropriate technologies to engage students and support diversity</span><span class="c-excellent"></span></div></div>

<div class="standard col-2" style="top:504px"><p class="standard-title">6. Students are provided with opportunities to interact with staff</p>
<div class="rubric"><span class="head h-threshold">Threshold</span><span class="head h-good">Good</span><span class="head h-excellent">Excellent</span><span class="c-threshold">Staff are provided with opportunities to answer student queries</span><span class="c-good">Staff are provided with opportunities to be active participants in learning-focused interactions</span><span class="c-excellent"></span></div></div>

<h2 class="section-title" style="top:626px">Two: Staff</h2>
<p class="section-intro" style="top:666px">Staff are supported in their online teaching with quality <b>professional development</b> [9], <b>resourcing</b> [10] and <b>technical support</b> [11].</p>

<div class="standard col-1" style="top:702px"><p class="standard-title tight">9. Staff are provided with quality professional development in online education</p>
<div class="rubric"><span class="head h-threshold">Threshold</span><span class="head h-good">Good</span><span class="head h-excellent">Excellent</span><span class="c-threshold">A range of appropriate, up-to-date and informative professional development activities are available to staff</span><span class="c-good">The organisation requires staff to engage in continued professional development relevant to online education</span><span class="c-excellent"></span></div></div>

<div class="standard col-2" style="top:702px"><p class="standard-title">10. Online education is recognised in workload</p>
<div class="rubric"><span class="head h-threshold">Threshold</span><span class="head h-good">Good</span><span class="head h-excellent">Excellent</span><span class="c-threshold">Online teaching is recognised in workload</span><span class="c-good">Online unit development is recognised in workload</span><span class="c-excellent"></span></div></div>

<div class="standard col-3" style="top:702px"><p class="standard-title">11. Staff are supported in their use of educational technology</p>
<div class="rubric"><span class="head h-threshold">Threshold</span><span class="head h-good">Good</span><span class="head h-excellent">Excellent</span><span class="c-threshold">Appropriate, up-to-date and reliable technological guides and resources are provided online</span><span class="c-good">Appropriate, timely and reliable asynchronous technological support is available</span><span class="c-excellent"></span></div></div>

<h2 class="section-title" style="top:826px">Three: Organisation</h2>
<p class="section-intro" style="top:866px">The organisation supports online education through the provision of quality <b>leadership</b> [12-13], <b>infrastructure</b> [14] and <b>evaluation</b> [15-17]</p>

<div class="standard col-1" style="top:901px"><p class="standard-title two-line">12. The organisation provides strategic leadership in online education</p>
<div class="rubric"><span class="head h-threshold">Threshold</span><span class="head h-good">Good</span><span class="head h-excellent">Excellent</span><span class="c-threshold">The organisation has a clearly articulated strategic position on online education</span><span class="c-good">An appropriate member of the executive has explicit responsibility for online education</span><span class="c-excellent"></span></div></div>

<div class="standard col-2" style="top:901px"><p class="standard-title two-line">14. The organisation maintains and supports a quality learning platform for delivering online education</p>
<div class="rubric"><span class="head h-threshold">Threshold</span><span class="head h-good">Good</span><span class="head h-excellent">Excellent</span><span class="c-threshold">The organisation maintains and supports an appropriate learning platform</span><span class="c-good">The learning platform provided is fit for purpose, scalable and reliable</span><span class="c-excellent"></span></div></div>

<div class="standard col-3" style="top:901px"><p class="standard-title two-line">16. The organisation has a process for evaluating and improving training and support for staff</p>
<div class="rubric"><span class="head h-threshold">Threshold</span><span class="head h-good">Good</span><span class="head h-excellent">Excellent</span><span class="c-threshold">The organisation has a systematic process for evaluating and improving staff training and support</span><span class="c-good">The organisation has a systematic process for improving staff training and support and communicating improvements to staff</span><span class="c-excellent"></span></div></div>

<div class="standard col-1" style="top:1021px"><p class="standard-title two-line">13. The organisation employs a systematic approach to resource allocation in online education</p>
<div class="rubric"><span class="head h-threshold">Threshold</span><span class="head h-good">Good</span><span class="head h-excellent">Excellent</span><span class="c-threshold">There is a systematic approach to resource allocation</span><span class="c-good">There is systematic approach with formal criteria that are widely available</span><span class="c-excellent"></span></div></div>

<div class="standard col-2" style="top:1021px"><p class="standard-title two-line">15. The organisation has a process for evaluating and improving student satisfaction with online education</p>
<div class="rubric"><span class="head h-threshold">Threshold</span><span class="head h-good">Good</span><span class="head h-excellent">Excellent</span><span class="c-threshold">The organisation has a systematic process for evaluating and improving student satisfaction with online education</span><span class="c-good" style="font-size:5.6px;line-height:7px">The organisation has a systematic process for improving student learning outcomes and satisfaction with online education and communicating improvements to students</span><span class="c-excellent"></span></div></div>

<div class="standard col-3" style="top:1021px"><p class="standard-title two-line">17. The organisation has a process for evaluating and improving infrastructure</p>
<div class="rubric"><span class="head h-threshold">Threshold</span><span class="head h-good">Good</span><span class="head h-excellent">Excellent</span><span class="c-threshold">The organisation has a systematic process for evaluating and improving infrastructure</span><span class="c-good">The organisation has a systematic process for improving infrastructure and communicating improvements to stakeholders</span><span class="c-excellent"></span></div></div>

<footer>
  <div class="licence"><div class="licence-mark"></div><div class="licence-name">open share</div></div>
  <p class="licence-text">This work is licensed under the Open Share Licence Attribution-ShareAlike 3.0 terms. To view a copy of this licence, visit the licence website or send a letter to Open Share Licence, 18 Larkmoor Lane, Suite 4, Fenwick, 50210. Support for this activity has been provided by the National Office for Tertiary Teaching. The views expressed in this activity do not necessarily reflect the views of the National Office for Tertiary Teaching.</p>
</footer>
</body>
</html>
```